TR Dowsett Carpentry car wrap design

We need a design that will go on a 2009 Hyundia iLoad and Toyota Hilux.
The back ground should look like clean crisp composite decking that is charcoal and then we want our logo in the same spot on both vehicles.
I want to draw traffic to my website so you will notice onb the skecth there is :
FOR INSTANT ESTIMATES
VISIT
trdowsettcarpentry.example.au

Target Market(s)

Families wanting to upgrade their outdoor living area

Industry/Entity Type

Carpentry

Font styles to use
Serif

Colors

Designer to choose colors to be used in the design.

Requirements
Must have
• be attractive and attention seeking
Nice to have
• clarity
Should not have
• be blurred or confusing.

```html
<!DOCTYPE html>
<html lang="en">
<head>
<meta charset="utf-8">
<title>TR Dowsett Carpentry – Vehicle Wrap</title>
<link href="https://fonts.googleapis.com/css2?family=Oswald:wght@400;500;600&display=swap" rel="stylesheet">
<style>
  :root {
    --backdrop: #dd3749;
    --charcoal: #3a3a3c;
    --charcoal-deep: #2b2b2d;
    --panel-white: #f7f7f7;
    --brand-red: #c8222f;
    --text-light: #f2f2f2;
    --text-dark: #3b3b3d;
  }
  * { margin: 0; padding: 0; box-sizing: border-box; }
  html, body { width: 1200px; height: 1200px; overflow: hidden; }
  body {
    background: var(--backdrop);
    font-family: "Oswald", "Arial Narrow", sans-serif;
    position: relative;
  }
  .wrap-layout {
    position: absolute;
    left: 127px;
    top: 490px;
    width: 973px;
    height: 220px;
    display: flex;
    box-shadow: 0 18px 30px rgba(0,0,0,0.25);
  }
  .rear-panel {
    width: 308px;
    background: linear-gradient(180deg, var(--charcoal) 0%, var(--charcoal-deep) 100%);
    padding: 46px 0 0 30px;
    color: var(--text-light);
  }
  .phone-line {
    display: flex;
    align-items: center;
    gap: 10px;
    font-size: 42px;
    font-weight: 500;
    line-height: 1;
  }
  .phone-icon { width: 32px; height: 32px; flex: none; }
  .contact-label {
    margin-top: 12px;
    color: var(--brand-red);
    font-size: 22px;
    line-height: 1.1;
    text-transform: uppercase;
  }
  .service-list {
    list-style: none;
    font-size: 23px;
    line-height: 1.1;
    text-transform: uppercase;
  }
  .door-panel {
    width: 285px;
    background: var(--panel-white);
    position: relative;
    color: var(--text-dark);
    text-transform: uppercase;
  }
  .accent-bar {
    position: absolute;
    left: 0;
    top: 96px;
    width: 112px;
    height: 22px;
    background: var(--brand-red);
  }
  .estimate-copy {
    position: absolute;
    right: 18px;
    top: 64px;
    text-align: right;
    line-height: 1.15;
  }
  .estimate-heading { color: var(--brand-red); font-size: 23px; font-weight: 500; }
  .estimate-visit { font-size: 23px; margin-top: 2px; }
  .estimate-url { font-size: 19.5px; letter-spacing: -0.3px; margin-top: 2px; }
  .logo-panel {
    width: 295px;
    background: linear-gradient(180deg, var(--charcoal) 0%, var(--charcoal-deep) 100%);
    display: flex;
    align-items: center;
    gap: 12px;
    padding-left: 24px;
  }
  .brand-square {
    width: 14px;
    height: 14px;
    background: var(--brand-red);
    flex: none;
  }
  .brand-name {
    color: var(--text-light);
    font-size: 22px;
    font-weight: 500;
    line-height: 1;
    text-transform: uppercase;
    white-space: nowrap;
  }
  .front-panel {
    flex: 1;
    background: var(--panel-white);
  }
</style>
</head>
<body>
  <main class="wrap-layout">
    <section class="rear-panel">
      <div class="phone-line">
        <svg class="phone-icon" viewBox="0 0 24 24" aria-hidden="true">
          <path fill="#f2f2f2" d="M6.6 10.8a15.1 15.1 0 0 0 6.6 6.6l2.2-2.2a1 1 0 0 1 1-.25 11.4 11.4 0 0 0 3.6.57 1 1 0 0 1 1 1V20a1 1 0 0 1-1 1A17 17 0 0 1 3 4a1 1 0 0 1 1-1h3.5a1 1 0 0 1 1 1c0 1.250.2 2.450.57 3.6a1 1 0 0 1-.25 1z"/>
        </svg>
        <span class="phone-number">0412345678</span>
      </div>
      <p class="contact-label">Contact for</p>
      <ul class="service-list">
        <li>Decks</li>
        <li>Pergolas</li>
      </ul>
    </section>
    <section class="door-panel">
      <div class="accent-bar"></div>
      <div class="estimate-copy">
        <p class="estimate-heading">For instant estimates</p>
        <p class="estimate-visit">Visit</p>
        <p class="estimate-url">trdowsettcarpentry.example.au</p>
      </div>
    </section>
    <section class="logo-panel">
      <span class="brand-square"></span>
      <span class="brand-name">TR Dowsett Carpentry</span>
    </section>
    <section class="front-panel"></section>
  </main>
</body>
</html>
```